Consulting Group Website Landing Page Design

We are working with a Consulting Group in California. They provide consulting services to law enforcement agencies throughout the US.
Some sites to use for content:
https://www.marlowcrestcenter.org
https://www.jpellingroup.com
https://www.48rkventures.com
https://www.vdq.org
http://www.themirvalgroup.com
Thank you for taking the time to consider designing a website for us. We are web developers based in Stockton, CA, USA. Most of our projects go through the same process. Understanding this process may help you win a project with us. We custom-code all of our websites in-house. We don’t have any requirements as to what tools you use for your design, but we ask that you follow these guidelines. Plus, please send your designs in at least 1200px. wide so they do not pixelate when we show the client.
IMAGES:
If you use any images or icons in the design, we ask that you have a link to the asset so we can purchase the image/icon. Most of the designs we submit do not have the customer’s images on them unless they have some great images. Be creative; show us the feeling you are trying to portray with your image choices. Use any royalty-free site you choose. We subscribe to Velmora and mainly use their images, but we can purchase images outside of Velmora. PLEASE NOTE: we will not submit designs to clients with watermarks on the images.
FONTS:
We ask that you identify the fonts you’re using in the design. This can be done in a message if you want. We typically use Quintet Fonts and Velmora Fonts.
CONTENT:
We're always open to different content and ideas. We often submit designs with stock images so the client can see our vision. We typically take pictures after the website launch to use their images with our vision. Lorem Ipsum is fine for paragraphs, but we ask that you make the Headers with correct English. We want to be able to show the vision and identify the sections of the website.
INSPIRATION:
We typically add a couple of links in the brief of websites we like to help you get started in your design.
REVISIONS:
We do not often ask for revisions of the designs unless we see something in the design that may not appeal to the client. If there are slight changes that we want to make, we do that in the development process.
FEEDBACK:
We rarely give feedback on designs during the design process. We are working on many website projects and do not have the time to provide feedback. We usually respond if your request is well thought out and asks specific questions, but a note asking “feedback, please” usually goes unanswered.

```html
<!DOCTYPE html>
<html lang="en">
<head>
<meta charset="utf-8">
<title>Northgate Advisory — Police &amp; Public Practices Consulting</title>
<link rel="stylesheet" href="https://fonts.googleapis.com/css2?family=Poppins:wght@500;600&family=Roboto:wght@400;500;700&family=Tinos&display=swap">
<style>
:root{
  --green:#6fb02a;
  --blue:#0b4d93;
  --dark:#1e1f23;
  --ink:#222;
  --muted:#6b6b6b;
  --light:#eef0f4;
  --white:#fff;
}
*{box-sizing:border-box;margin:0;padding:0}
html,body{width:1200px;height:4649px;overflow:hidden}
body{font-family:'Tinos',serif;color:var(--ink);background:var(--white);position:relative}
section,header,footer{position:absolute;left:0;width:1200px}
.abs{position:absolute}
.heading{font-family:'Poppins',sans-serif;font-weight:500}
.btn{position:absolute;display:flex;align-items:center;justify-content:center;background:var(--green);color:var(--white);font:700 14px 'Roboto',sans-serif}
.label{position:absolute;display:flex;align-items:center}
.label::before{content:"";width:72px;height:2px;background:var(--blue)}
.label span{background:var(--blue);color:var(--white);font:500 17px 'Roboto',sans-serif;padding:3px 10px;letter-spacing:.3px}
.photo{position:absolute}

/* hero */
.hero{top:0;height:686px;background:linear-gradient(160deg,#2c3038 0%,#15171b 55%,#24262a 100%)}
.brand{position:absolute;display:flex;align-items:center;gap:8px;font:500 19px 'Roboto',sans-serif;color:#fff}
.brand i{display:block;width:22px;height:22px;border-radius:50%;background:var(--blue);border:2px solid var(--green)}
.nav{position:absolute;top:33px;font:500 14px 'Roboto',sans-serif;color:#fff}
.nav.active{color:var(--green)}
.hero h1{position:absolute;top:232px;width:100%;text-align:center;color:#fff;font:600 63px/64px 'Poppins',sans-serif;letter-spacing:-1px}
.hero p{position:absolute;top:382px;left:195px;width:810px;text-align:center;color:#fff;font-size:16px;line-height:23px}

/* about */
.about{top:686px;height:781px;background:#fff}
.about h2{position:absolute;top:170px;left:108px;color:var(--green);font-size:41px;line-height:44px}
.about p{position:absolute;top:278px;left:108px;width:480px;color:var(--muted);font-size:15.5px;line-height:22.5px}
.about .frame{position:absolute;left:688px;top:116px;width:368px;height:368px;border-radius:50%;border:14px solid var(--blue)}
.stat{position:absolute;top:578px;width:200px;text-align:center}
.stat b{display:block;font:500 48px 'Roboto',sans-serif;color:var(--green)}
.stat small{font:700 14px 'Roboto',sans-serif;color:var(--ink)}
.divider{position:absolute;top:570px;width:1px;height:95px;background:#e4e4e4}

/* cta */
.cta{top:1467px;height:593px;background:linear-gradient(120deg,#3a3c40,#25272b 60%,#34363a)}
.cta h2{position:absolute;top:138px;width:100%;text-align:center;color:#fff;font-size:41px;line-height:43px}
.cta p{position:absolute;top:332px;left:310px;width:580px;text-align:center;color:#fff;font-size:15.5px;line-height:22px}

/* services */
.services{top:2060px;height:897px;background:var(--light)}
.services h2{position:absolute;top:183px;left:69px;color:var(--green);font-size:40px;line-height:44px}
.services .intro{position:absolute;top:288px;left:69px;width:300px;color:var(--muted);font-size:14.5px;line-height:22px}
.card{position:absolute;width:345px;height:314px;background:#fff;box-shadow:0 4px 14px rgba(0,0,0,.08);text-align:center}
.card .icon{position:absolute;top:29px;left:142px;width:61px;height:61px;background:var(--green);display:flex;align-items:center;justify-content:center}
.card h3{position:absolute;top:112px;width:100%;font:500 22px 'Roboto',sans-serif;color:var(--ink)}
.card p{position:absolute;top:152px;left:26px;width:293px;color:var(--muted);font-size:14.5px;line-height:22px}
.card .more{position:absolute;bottom:0;left:0;width:100%;height:45px;background:var(--blue);color:#fff;display:flex;align-items:center;justify-content:center;font:700 14px 'Roboto',sans-serif}

/* reviews */
.reviews{top:2957px;height:612px;background:linear-gradient(140deg,#3c3f44,#2a2c30 55%,#3b3d41)}
.reviews h2{position:absolute;top:137px;left:54px;color:#fff;font-size:40px}
.review{position:absolute;top:243px;width:347px;height:217px;background:rgba(235,237,240,.92)}
.review p{position:absolute;top:20px;left:19px;width:300px;font:400 13.5px/21px 'Roboto',sans-serif;color:#555}
.review .avatar{position:absolute;top:127px;left:19px;width:64px;height:64px;border-radius:50%;border:3px solid var(--green);background:linear-gradient(#c7ccd3,#8e97a3)}
.review b{position:absolute;top:140px;left:103px;font:700 15px 'Tinos',serif;color:var(--ink)}
.review small{position:absolute;top:163px;left:103px;font-size:13px;color:#888}
.dot{position:absolute;top:3437px;width:8px;height:8px;border-radius:50%;background:#9bb3d3}

/* contact */
.contact{top:3569px;height:647px;background:#fff}
.form-panel{position:absolute;top:61px;left:60px;width:539px;height:599px;background:#fff;border-bottom:4px solid var(--green);box-shadow:0 0 18px rgba(0,0,0,.06);z-index:2}
.form-panel h2{position:absolute;top:133px;left:45px;color:var(--green);font-size:40px;line-height:44px}
.field{position:absolute;background:#eef0f4;color:#8a8a8a;font-size:14px;padding:12px 15px}

/* footer */
.footer{top:4216px;height:433px;background:var(--dark);color:#fff}
.footer h4{position:absolute;top:99px;font:700 17px 'Roboto',sans-serif}
.footer h4::after{content:"";display:inline-block;width:18px;height:2px;background:var(--green);margin-left:6px;vertical-align:-2px}
.footer ul{position:absolute;top:145px;list-style:none;font-size:14.5px;line-height:29px}
.social{position:absolute;top:138px;width:14px;height:14px;border-radius:50%;border:2px solid #fff}
.copy{position:absolute;top:388px;left:63px;font-size:12.5px}
</style>
</head>
<body>

<header class="hero">
  <div class="photo" role="img" aria-label="Dark night street scene with a police car" style="inset:0;background:radial-gradient(ellipse at 75% 60%,#4a4c50 0%,transparent 55%)"></div>
  <div class="brand" style="top:26px;left:63px"><i></i>Northgate Advisory</div>
  <span class="nav active" style="left:397px">Home</span>
  <span class="nav" style="left:486px">About Us</span>
  <span class="nav" style="left:594px">Services</span>
  <span class="nav" style="left:699px">Contact Us</span>
  <div class="btn" style="left:967px;top:22px;width:170px;height:43px;font-size:14px;gap:6px">
    <svg width="13" height="13" viewBox="0 0 24 24"><path fill="#fff" d="M6.6 10.8a15 15 0 0 0 6.6 6.6l2.2-2.2a1 1 0 0 1 1-.25 11.4 11.4 0 0 0 3.6.57 1 1 0 0 1 1 1V20a1 1 0 0 1-1 1A17 17 0 0 1 3 4a1 1 0 0 1 1-1h3.5a1 1 0 0 1 1 1c0 1.25.2 2.45.57 3.6a1 1 0 0 1-.25 1z"/></svg>(555) 010 4567</div>
  <h1>Police &amp; Public Practices<br>Consulting Services</h1>
  <p>Police and public organizations have all kinds of difficult and extremely complex internal and external challenges thrown your way. You need advice that mitigates risks, protects public investments, and drives maximum value to community stakeholders.</p>
  <div class="btn" style="left:495px;top:471px;width:204px;height:49px">Make an Appointment</div>
</header>

<section class="about">
  <div class="label" style="left:108px;top:130px"><span>ABOUT US</span></div>
  <h2 class="heading">Police &amp; Public Practices<br>Consulting Services</h2>
  <p>Integer luctus duis iaculis consequat arcu tortor. Convallis curae primis massa in aenean dui hendrerit. Gravida nostra vel at leo porta mattis montes congue dictumst arcu. Quis enim etiam cras potenti integer ut erat vestibulum orci maecenas. Sodales efficitur senectus amet ut malesuada scelerisque elit finibus.</p>
  <div class="btn" style="left:108px;top:424px;width:143px;height:42px">Discover More</div>
  <div class="frame"></div>
  <div class="photo" role="img" aria-label="Team of consultants working at a laptop in an office" style="left:712px;top:140px;width:320px;height:320px;border-radius:50%;background:linear-gradient(135deg,#d9dde2,#8e959e 60%,#5a5f66)"></div>
  <div class="stat" style="left:91px"><b>95%</b><small>Happy Clients</small></div>
  <div class="divider" style="left:328px"></div>
  <div class="stat" style="left:364px"><b>387+</b><small>Cases Done</small></div>
  <div class="divider" style="left:601px"></div>
  <div class="stat" style="left:637px"><b>20+</b><small>Yrs Experience</small></div>
  <div class="divider" style="left:873px"></div>
  <div class="stat" style="left:909px"><b>45</b><small>Expert Coach</small></div>
</section>

<section class="cta">
  <div class="photo" role="img" aria-label="Professionals meeting around a screen showing charts" style="inset:0;background:radial-gradient(ellipse at 60% 40%,rgba(120,120,120,.35),transparent 60%)"></div>
  <h2 class="heading">Leading innovators in<br>building trust and respect<br>between communities and<br>public safety providers</h2>
  <p>Lorem ipsum dolor sit amet, consectetur adipiscing elit. Ut elit tellus, luctus nec ullamcorper mattis, pulvinar dapibus leo.</p>
  <div class="btn" style="left:523px;top:410px;width:154px;height:45px">Contact Us Now</div>
</section>

<section class="services">
  <div class="label" style="left:69px;top:142px"><span>OUR SERVICES</span></div>
  <h2 class="heading">Public Safety<br>Advisers</h2>
  <p class="intro">Eu netus tellus habitasse nibh malesuada. Rutrum vestibulum turpis faucibus suspendisse non vehicula integer id.</p>

  <div class="card" style="left:428px;top:126px">
    <div class="icon"><svg width="30" height="24" viewBox="0 0 30 24"><rect x="4" y="2" width="22" height="15" fill="none" stroke="#fff" stroke-width="2"/><rect x="1" y="19" width="28" height="3" fill="#fff"/></svg></div>
    <h3>Systems Assessment</h3>
    <p>Ultricies porttitor diam urna nisi efficitur magna mollis nunc taciti pulvinar. Nam at nisi dui id facilisis sapien luctus congue euismod aptent lobortis.</p>
    <div class="more">Learn More</div>
  </div>
  <div class="card" style="left:792px;top:126px">
    <div class="icon"><svg width="26" height="30" viewBox="0 0 26 30"><rect x="7" y="2" width="12" height="6" fill="#fff"/><circle cx="13" cy="13" r="5" fill="#fff"/><path d="M2 29 Q2 19 13 19 Q24 19 24 29Z" fill="#fff"/></svg></div>
    <h3>Policy Analysis</h3>
    <p>Ultricies porttitor diam urna nisi efficitur magna mollis nunc taciti pulvinar. Nam at nisi dui id facilisis sapien luctus congue euismod aptent lobortis.</p>
    <div class="more">Learn More</div>
  </div>
  <div class="card" style="left:63px;top:460px">
    <div class="icon"><svg width="28" height="28" viewBox="0 0 28 28"><rect x="3" y="4" width="22" height="21" fill="none" stroke="#fff" stroke-width="2"/><path d="M3 10h22M9 1v6M14 1v6M19 1v6" stroke="#fff" stroke-width="2"/></svg></div>
    <h3>Independent Investigations</h3>
    <p>Ultricies porttitor diam urna nisi efficitur magna mollis nunc taciti pulvinar. Nam at nisi dui id facilisis sapien luctus congue euismod aptent lobortis.</p>
    <div class="more">Learn More</div>
  </div>
  <div class="card" style="left:428px;top:460px">
    <div class="icon"><svg width="32" height="28" viewBox="0 0 32 28"><path d="M2 3h18v12H9l-5 4v-4H2z" fill="none" stroke="#fff" stroke-width="2"/><path d="M12 18h10l5 4v-4h3V7h-6" fill="none" stroke="#fff" stroke-width="2"/><path d="M6 8h10M6 11h7" stroke="#fff" stroke-width="2"/></svg></div>
    <h3>Management Consulting</h3>
    <p>Ultricies porttitor diam urna nisi efficitur magna mollis nunc taciti pulvinar. Nam at nisi dui id facilisis sapien luctus congue euismod aptent lobortis.</p>
    <div class="more">Learn More</div>
  </div>
  <div class="card" style="left:792px;top:460px">
    <div class="icon"><svg width="32" height="28" viewBox="0 0 32 28"><rect x="6" y="2" width="24" height="17" fill="none" stroke="#fff" stroke-width="2"/><circle cx="8" cy="15" r="4" fill="#fff"/><path d="M1 27 Q1 20 8 20 Q15 20 15 27Z" fill="#fff"/><path d="M12 14l8-5" stroke="#fff" stroke-width="2"/></svg></div>
    <h3>Training</h3>
    <p>Ultricies porttitor diam urna nisi efficitur magna mollis nunc taciti pulvinar. Nam at nisi dui id facilisis sapien luctus congue euismod aptent lobortis.</p>
    <div class="more">Learn More</div>
  </div>
</section>

<section class="reviews">
  <div class="photo" role="img" aria-label="Police officers in uniform, dimmed background" style="inset:0;background:radial-gradient(ellipse at 55% 20%,rgba(140,140,140,.3),transparent 55%)"></div>
  <div class="abs" style="left:54px;top:106px;width:140px;height:2px;background:var(--blue)"></div>
  <div class="abs" style="left:194px;top:94px;background:var(--blue);color:#fff;font:500 17px 'Roboto',sans-serif;padding:3px 10px">OUR SERVICES</div>
  <h2 class="heading">Our Clients Reviews</h2>
  <div class="abs" style="left:975px;top:138px;width:105px;height:1px;background:#888"></div>
  <svg class="abs" style="left:1090px;top:120px" width="48" height="36" viewBox="0 0 48 36"><path d="M2 2h18v16l-8 16H5l6-14H2zM28 2h18v16l-8 16h-7l6-14h-9z" fill="#6fb02a"/></svg>

  <div class="review" style="left:54px"><p>"Porttitor integer bibendum odio pulvinar rutrum magnis viverra orci tincidunt efficitur. Aptent pharetra est nunc mattis donec per mi porttitor penatibus."</p><div class="avatar" role="img" aria-label="Client portrait"></div><b>Dana R. Whitlock</b><small>Manager</small></div>
  <div class="review" style="left:426px"><p>"Porttitor integer bibendum odio pulvinar rutrum magnis viverra orci tincidunt efficitur. Aptent pharetra est nunc mattis donec per mi porttitor penatibus."</p><div class="avatar" role="img" aria-label="Client portrait"></div><b>Calder Finch</b><small>Trader</small></div>
  <div class="review" style="left:798px"><p>"Porttitor integer bibendum odio pulvinar rutrum magnis viverra orci tincidunt efficitur. Aptent pharetra est nunc mattis donec per mi porttitor penatibus."</p><div class="avatar" role="img" aria-label="Client portrait"></div><b>Warren T. Ashby</b><small>Accountant</small></div>
</section>
<div class="dot" style="left:575px"></div>
<div class="dot" style="left:596px;background:var(--green)"></div>
<div class="dot" style="left:617px"></div>

<section class="contact">
  <div class="photo" role="img" aria-label="Smiling consultant holding a clipboard in an office with bookshelves" style="left:601px;top:75px;width:538px;height:572px;background:linear-gradient(135deg,#7a6a58,#a59885 45%,#4f6587)"></div>
  <div class="form-panel">
    <div class="label" style="left:45px;top:95px"><span>CONTACT US</span></div>
    <h2 class="heading">Make your<br>appointment</h2>
    <div class="field" style="left:45px;top:240px;width:220px;height:42px">Name</div>
    <div class="field" style="left:274px;top:240px;width:220px;height:42px">Phone</div>
    <div class="field" style="left:45px;top:294px;width:220px;height:42px">Email</div>
    <div class="field" style="left:274px;top:294px;width:220px;height:42px;color:#555">Financial Technology
      <svg class="abs" style="right:14px;top:17px" width="10" height="6" viewBox="0 0 10 6"><path d="M0 0h10L5 6z" fill="#555"/></svg></div>
    <div class="field" style="left:45px;top:345px;width:449px;height:95px">Message</div>
    <div class="btn" style="left:45px;top:453px;width:449px;height:47px">Make an Appointment</div>
  </div>
</section>

<footer class="footer">
  <div class="brand" style="top:138px;left:72px;font-size:30px;gap:10px"><i style="width:40px;height:40px;border-width:3px"></i>Northgate Advisory</div>
  <h4 style="left:435px">Information</h4>
  <ul style="left:435px"><li>History</li><li>Contact Us</li><li>Leadership</li><li>Careers</li><li>News &amp; Article</li></ul>
  <h4 style="left:653px">Services</h4>
  <ul style="left:653px"><li>Coaching</li><li>Consulting</li><li>Advisory</li><li>Online Course</li><li>Certification</li></ul>
  <h4 style="left:872px">Follow Us</h4>
  <span class="social" style="left:872px"></span>
  <span class="social" style="left:912px"></span>
  <span class="social" style="left:952px"></span>
  <span class="social" style="left:992px"></span>
  <p class="copy">Copyright © 2023 Northgate Advisory, All rights reserved.</p>
</footer>

</body>
</html>
```